KV MOTORS BANNER/SIGN DESIGN

Design a banner sign for outdoor use for KV MOTORS - a premium pre owned vehicle sales center. The size must be 36 feet in width
and 3 feet in height.

Information required: logo (attached)
-PREMIUM PRE-OWEND VEHICLE SALES
- 403.555.0172

perhaps in smaller font: BUY-SELL-TRADE

prefer white background but could possibly do red matching the logo

```html
<!DOCTYPE html>
<html lang="en">
<head>
<meta charset="utf-8">
<title>KV Motors Banner – D5</title>
<link rel="stylesheet" href="https://fonts.googleapis.com/css2?family=Archivo:wdth,wght@62..125,100..900&family=Oswald:wght@500;600;700&family=Zilla+Slab:wght@700&display=swap">
<style>
  :root {
    --paper: #ffffff;
    --night: #0b0c0b;
    --ink: #111111;
    --brand-red: #e0262a;
    --frame-light: #d9d9d9;
  }
  * { margin: 0; padding: 0; box-sizing: border-box; }
  html, body {
    width: 1200px;
    height: 667px;
    overflow: hidden;
    background: var(--paper);
  }
  .canvas {
    position: relative;
    width: 1200px;
    height: 667px;
  }
  .panel-light {
    position: absolute;
    inset: 0 0 auto 0;
    height: 359px;
    background: var(--paper);
  }
  .panel-dark {
    position: absolute;
    left: 0; right: 0; bottom: 0;
    height: 308px;
    background: var(--night);
  }
  .option-label {
    position: absolute;
    left: 249px;
    top: 103px;
    font-family: "Oswald", sans-serif;
    font-weight: 700;
    font-size: 26px;
    line-height: 1;
    color: var(--ink);
  }
  .banner {
    position: absolute;
    left: 251px;
    width: 693px;
    height: 59px;
    display: block;
  }
  .banner--on-light { top: 160px; }
  .banner--on-dark { top: 466px; }

  .banner .sign-board { fill: var(--paper); }
  .banner--on-light .sign-board { stroke: var(--ink); stroke-width: 1.5; }
  .banner--on-dark .sign-board { stroke: var(--frame-light); stroke-width: 1; }

  .brand-dot { fill: none; stroke: var(--brand-red); stroke-width: 2.5; }
  .brand-name {
    font-family: "Archivo", sans-serif;
    font-weight: 900;
    font-stretch: 125%;
    font-size: 30px;
    fill: var(--ink);
  }
  .tagline {
    font-family: "Zilla Slab", serif;
    font-weight: 700;
    font-size: 20px;
    fill: var(--ink);
  }
  .tagline .accent { fill: var(--brand-red); }
  .divider { stroke: var(--ink); stroke-width: 2; }
  .headline {
    font-family: "Oswald", sans-serif;
    font-weight: 600;
    font-size: 29px;
    fill: var(--brand-red);
  }
  .phone {
    font-family: "Archivo", sans-serif;
    font-weight: 900;
    font-stretch: 125%;
    font-size: 20px;
    fill: var(--ink);
  }
</style>
</head>
<body>
<main class="canvas">
  <div class="panel-light"></div>
  <div class="panel-dark"></div>

  <p class="option-label">D5</p>

  <svg class="banner banner--on-light" viewBox="0 0 693 59" aria-label="KV Motors banner on white">
    <rect class="sign-board" x="0.75" y="0.75" width="691.5" height="57.5" rx="1"/>
    <circle class="brand-dot" cx="34" cy="22" r="14"/>
    <text class="brand-name" x="56" y="35" textLength="196" lengthAdjust="spacingAndGlyphs">KV MOTORS</text>
    <text class="tagline" x="18" y="55" textLength="236" lengthAdjust="spacingAndGlyphs">BUY-<tspan class="accent">SELL</tspan>-TRADE</text>
    <line class="divider" x1="272" y1="9" x2="272" y2="55"/>
    <text class="headline" x="287" y="33" textLength="388" lengthAdjust="spacingAndGlyphs">PREMIUM PRE-OWEND VEHICLE SALES</text>
    <text class="phone" x="287" y="55" textLength="388" lengthAdjust="spacingAndGlyphs">403.555.0172</text>
  </svg>

  <svg class="banner banner--on-dark" viewBox="0 0 693 59" aria-label="KV Motors banner on black">
    <rect class="sign-board" x="0.5" y="0.5" width="692" height="58"/>
    <circle class="brand-dot" cx="34" cy="22" r="14"/>
    <text class="brand-name" x="56" y="35" textLength="196" lengthAdjust="spacingAndGlyphs">KV MOTORS</text>
    <text class="tagline" x="18" y="55" textLength="236" lengthAdjust="spacingAndGlyphs">BUY-<tspan class="accent">SELL</tspan>-TRADE</text>
    <line class="divider" x1="272" y1="9" x2="272" y2="55"/>
    <text class="headline" x="287" y="33" textLength="388" lengthAdjust="spacingAndGlyphs">PREMIUM PRE-OWEND VEHICLE SALES</text>
    <text class="phone" x="287" y="55" textLength="388" lengthAdjust="spacingAndGlyphs">403.555.0172</text>
  </svg>
</main>
</body>
</html>
```